Criação de Papelaria (6 itens) para Arquitetura
" Trata-se de uma empresa do ramo de arquitetura e urbanismo, formada por um casal de jovens arquitetos. Os serviços podem ser prestados presencialmente através do contato direto com o cliente ou ainda por meio da internet, onde a abordagem com o cliente se dá através das redes sociais. A empresa pretende ampliar sua atuação na internet através do marketing digital e para isto necessita transmitir com clareza valores como: credibilidade, contemporaneidade, versatilidade e objetividade. "

```html
<!DOCTYPE html>
<html lang="pt-BR">
<head>
<meta charset="utf-8">
<title>Travessa Arquitetura e Interiores — Cartão de visita</title>
<link rel="stylesheet" href="https://fonts.googleapis.com/css2?family=Montserrat:wght@400;500;600;700&display=swap">
<style>
  :root {
    --page-bg: #e4e4e6;
    --card-dark: #3b3b3e;
    --card-dark-deep: #2b2b2e;
    --card-light: #ffffff;
    --orange: #f26a21;
    --peach: #f9d9c6;
    --grey-band: #dcdcdc;
    --text-dark: #2a2a2a;
    --text-mid: #555555;
    --text-light: #ffffff;
    --rule: #c9c9c9;
  }
  * { box-sizing: border-box; margin: 0; padding: 0; }
  html, body {
    width: 1200px; height: 1200px; overflow: hidden;
    background: var(--page-bg);
    font-family: "Montserrat", sans-serif;
  }
  .sheet {
    width: 1200px; height: 1200px;
    display: flex; flex-direction: column; align-items: center; justify-content: center;
    gap: 60px;
  }
  .card {
    position: relative;
    width: 900px; height: 500px;
    border-radius: 36px;
    overflow: hidden;
    box-shadow: 0 10px 30px rgba(0,0,0,0.18);
  }

  /* Front (dark) */
  .card--front {
    background: linear-gradient(135deg, var(--card-dark) 0%, var(--card-dark) 55%, var(--card-dark-deep) 100%);
  }
  .front__edge {
    position: absolute; left: 0; top: 230px; bottom: 0; width: 22px;
    background: var(--orange);
  }
  .front__web {
    position: absolute; top: 30px; left: 0; right: 0;
    text-align: center;
    color: rgba(255,255,255,0.55);
    font-size: 15px; letter-spacing: 3px;
  }
  .brand {
    position: absolute; left: 0; right: 0; top: 150px;
    display: flex; flex-direction: column; align-items: center;
  }
  .brand__row { display: flex; align-items: center; gap: 22px; }
  .brand__dot {
    width: 62px; height: 62px; border-radius: 50%;
    background: var(--orange);
  }
  .brand__name {
    color: var(--text-light);
    font-size: 86px; font-weight: 600; letter-spacing: 6px;
    line-height: 1;
  }
  .brand__tagline {
    margin-top: 18px;
    color: var(--orange);
    font-size: 24px; font-weight: 400; letter-spacing: 1px;
  }

  /* Back (white) */
  .card--back { background: var(--card-light); }
  .back__band {
    position: absolute;
  }
  .back__band--peach {
    left: -60px; top: -40px; width: 420px; height: 120px;
    background: var(--peach);
    transform: rotate(-8deg);
  }
  .back__band--grey {
    left: 180px; top: -60px; width: 60px; height: 300px;
    background: var(--grey-band);
    transform: rotate(30deg);
    opacity: 0.8;
  }
  .back__brand {
    position: absolute; left: 60px; top: 170px; width: 340px;
    display: flex; flex-direction: column; align-items: center;
  }
  .back__brand .brand__dot { width: 40px; height: 40px; }
  .back__brand .brand__name {
    color: var(--text-mid); font-size: 50px; letter-spacing: 4px;
  }
  .back__brand .brand__tagline {
    margin-top: 10px; font-size: 15px;
  }
  .back__divider {
    position: absolute; left: 440px; top: 110px; bottom: 110px;
    width: 2px; background: var(--rule);
  }
  .contact {
    position: absolute; left: 480px; top: 100px; right: 40px;
    color: var(--text-dark);
  }
  .contact__name { font-size: 28px; font-weight: 700; }
  .contact__role { font-size: 22px; font-weight: 500; margin-top: 4px; }
  .contact__list { list-style: none; margin-top: 36px; }
  .contact__item {
    display: flex; align-items: center; gap: 16px;
    font-size: 18px; color: var(--text-mid);
    margin-bottom: 22px; line-height: 1.3;
  }
  .contact__icon {
    flex: none;
    width: 34px; height: 34px; border-radius: 50%;
    background: var(--orange);
    display: flex; align-items: center; justify-content: center;
  }
  .contact__icon svg { width: 18px; height: 18px; }
</style>
</head>
<body>
<main class="sheet">

  <section class="card card--front" aria-label="Frente do cartão">
    <div class="front__edge"></div>
    <p class="front__web">www.travessa.com.br</p>
    <div class="brand">
      <div class="brand__row">
        <span class="brand__dot"></span>
        <span class="brand__name">TRAVESSA</span>
      </div>
      <p class="brand__tagline">Arquitetura e Interiores</p>
    </div>
  </section>

  <section class="card card--back" aria-label="Verso do cartão">
    <div class="back__band back__band--peach"></div>
    <div class="back__band back__band--grey"></div>

    <div class="back__brand brand">
      <div class="brand__row">
        <span class="brand__dot"></span>
        <span class="brand__name">TRAVESSA</span>
      </div>
      <p class="brand__tagline">Arquitetura e Interiores</p>
    </div>

    <div class="back__divider"></div>

    <div class="contact">
      <p class="contact__name">Nome do Arquiteto</p>
      <p class="contact__role">Arquiteta - CAU A654321</p>
      <ul class="contact__list">
        <li class="contact__item">
          <span class="contact__icon">
            <svg viewBox="0 0 24 24" fill="#fff"><path d="M6.6 10.8a15 15 0 0 0 6.6 6.6l2.2-2.2a1 1 0 0 1 1-.25 11.4 11.4 0 0 0 3.6.57 1 1 0 0 1 1 1V20a1 1 0 0 1-1 1A17 17 0 0 1 3 4a1 1 0 0 1 1-1h3.5a1 1 0 0 1 1 1c0 1.25.2 2.45.57 3.57a1 1 0 0 1-.25 1z"/></svg>
          </span>
          (61) 95555-0142
        </li>
        <li class="contact__item">
          <span class="contact__icon">
            <svg viewBox="0 0 24 24" fill="#fff"><path d="M3 5h18v14H3z" opacity="0"/><path d="M3 6h18v12H3V6zm2 1.5v.3l7 4.7 7-4.7v-.3H5z"/></svg>
          </span>
          contato@travessa.com.br
        </li>
        <li class="contact__item">
          <span class="contact__icon">
            <svg viewBox="0 0 24 24" fill="#fff"><path d="M12 2a7 7 0 0 0-7 7c0 5.2 7 13 7 13s7-7.8 7-13a7 7 0 0 0-7-7zm0 9.5A2.5 2.5 0 1 1 12 6.5a2.5 2.5 0 0 1 0 5z"/></svg>
          </span>
          <span>Rua das Acácias 48 Jardim Alto<br>Vila Serena/MG CEP</span>
        </li>
      </ul>
    </div>
  </section>

</main>
</body>
</html>
```